Awsome new website

We are a Fencing Contracting company in Melbourne Australia. We supply and install Timer and Steel boundary fences as well as Pool fencing (e.g. glass, tubular steel). We also manufacture and install swing and sliding gates.

We want a new website that is a modern business website.
We are targeting domestic and business clients.
The design should compliment our logo and company name.
The website needs to be easy to update.

Some specifics we want.
Menu - Main menu at top of page and smaller footer menu (to add different menu items)
Slider - Main page to have a slider on it that's easy for us to add and remove slides.
Call to action - all pages to have a "call to action" logo or icon that attracts attention (see file "call_to_action.pdf)
Instant quote - we have a online quote page we need a distinctive logo or icon to redirect to this page.
Main page to have a product /Service guide (see file "website_idea.jpg")
Main page to have widgets or quick link to
o why choose us
o Brochures
o Gallery

Have a Gallery page formatted with different category galleries. e.g. Timber, Glass, Feature
Maintain the current link to our staff page with password, (link in footer menu)

Hopefully that covers everything.
Our current website is www.tallowcreekrails.com.au to have a look at the current site.
regards Doug

• Turn off blogging as we don’t want 100’s of comments from spammers to delete

We would like to implement the QX-Portal plugin (see "http://qx-portal-demo.net/" ), but this can be done after the new Theme has been implemented.

```html
<!DOCTYPE html>
<html lang="en">
<head>
<meta charset="utf-8">
<title>Tallow Creek Rails – Fencing Contractors</title>
<link href="https://fonts.googleapis.com/css2?family=Bebas+Neue&family=Montserrat:wght@700;800&family=Open+Sans:wght@400;600&family=Roboto+Condensed:wght@400;700&display=swap" rel="stylesheet">
<style>
:root{
  --red:#b80c0c;
  --red-dark:#8e0606;
  --navy:#2f3d52;
  --navy-light:#3c4b61;
  --cream:#ebe8e2;
  --paper:#f3f1ee;
  --text:#222;
  --grey-box:#e6e6e6;
  --footer:#3b4658;
  --footer-base:#2d3646;
  --tan:#c9a676;
}
*{box-sizing:border-box;margin:0;padding:0}
html,body{width:935px;height:1200px;overflow:hidden}
body{position:relative;background:var(--cream);font-family:"Open Sans",Arial,sans-serif;color:var(--text)}
.abs{position:absolute}

/* header */
.site-header{left:0;top:0;width:935px;height:92px;background:#eeebe6}
.brand{left:127px;top:20px;display:flex;align-items:center;gap:10px}
.brand-square{width:46px;height:46px;background:var(--red)}
.brand-name{font-family:"Bebas Neue",sans-serif;font-size:34px;color:var(--red);letter-spacing:1px;line-height:1}
.call-now{left:570px;top:10px;width:230px;height:75px}
.call-label{left:68px;top:9px;font-family:"Montserrat",sans-serif;font-weight:800;font-size:21px;color:var(--red);line-height:1;white-space:nowrap}
.call-number{left:47px;top:42px;font-family:"Bebas Neue",sans-serif;font-size:34px;color:var(--red);line-height:1;white-space:nowrap}

/* nav */
.main-nav{left:0;top:92px;width:935px;height:32px;background:var(--red)}
.main-nav ul{list-style:none;display:flex;position:absolute;left:126px;top:0;height:32px}
.main-nav li{font-family:"Roboto Condensed",sans-serif;font-size:14px;color:#fff;line-height:32px;padding:0 16px 0 11px;border-right:1px solid var(--red-dark);white-space:nowrap}
.main-nav li:last-child{border-right:0}

/* slider */
.hero{left:0;top:124px;width:935px;height:356px;background:linear-gradient(180deg,#c9d6c6 0%,#6d9a5c 30%,#8fc7d6 55%,#d8d5cc 72%,#5d9b3a 100%)}
.hero-title{left:138px;top:138px;width:440px;font-family:"Bebas Neue",sans-serif;font-weight:400;font-size:22px;line-height:18.5px;color:#111}
.hero-arrow{width:20px;height:20px;border-radius:50%;background:rgba(255,255,255,.45)}
.hero-dots{left:438px;top:418px;display:flex;gap:3px}
.hero-dots span{width:12px;height:11px;background:#fff}
.hero-dots span:first-child{background:var(--red)}

/* content */
.content{left:125px;top:433px;width:684px;height:580px;background:var(--paper)}
.h-welcome{left:138px;top:443px;font-family:"Montserrat",sans-serif;font-weight:800;font-size:20px;line-height:1;color:var(--navy);letter-spacing:.3px;white-space:nowrap}
.h-section{font-family:"Montserrat",sans-serif;font-weight:800;font-size:17px;line-height:1;color:var(--navy);white-space:nowrap}
.body-copy{font-size:8.4px;line-height:12px;color:#222}
.services{left:139px;top:604px;width:443px;height:143px;background:var(--grey-box);border:1px solid #c8c8c8}
.service-list{list-style:none;position:absolute;display:flex;flex-direction:column;gap:8.6px}
.service-list li{display:flex;align-items:center;gap:5px;font-family:"Bebas Neue",sans-serif;font-size:17px;color:#222;text-transform:uppercase;line-height:16px;white-space:nowrap;letter-spacing:.3px}
.quote-card{left:142px;top:930px;width:103px;height:64px;background:linear-gradient(#e6dcc6,#cdbc98);border:2px solid #8b6d3f}
.quote-banner{left:245px;top:938px;width:337px;height:51px;background:var(--tan);border:1px solid #a58654;font-family:"Bebas Neue",sans-serif;font-size:29px;color:#6b4f2e;line-height:53px;padding-left:6px;white-space:nowrap;overflow:hidden}

/* widgets */
.widget{left:596px;width:200px}
.widget-head{height:25px;background:var(--red);color:#fff;font-family:"Bebas Neue",sans-serif;font-size:23px;text-align:center;line-height:27px}
.widget-photo{height:63px}
.widget-body{height:63px;background:var(--grey-box);padding:5px 13px;font-size:7.6px;line-height:10.6px;color:#222;overflow:hidden}
.widget-btn{height:24px;background:var(--navy-light);position:relative;font-family:"Bebas Neue",sans-serif;font-size:17px;color:#fff;line-height:25px;padding-left:19px;white-space:nowrap}
.widget-btn .go{position:absolute;right:0;top:0;width:34px;height:24px;background:var(--red)}

/* footer */
.site-footer{left:0;top:1000px;width:935px;height:200px;background:var(--footer)}
.footer-base{left:0;top:1180px;width:935px;height:20px;background:var(--footer-base);color:#cfd3da;font-size:7px;text-align:center;line-height:20px;letter-spacing:.5px}
.footer-title{font-family:"Bebas Neue",sans-serif;font-weight:400;font-size:18px;line-height:1;color:#fff;white-space:nowrap}
.footer-menu{list-style:none;left:138px;top:1053px}
.footer-menu li{font-family:"Roboto Condensed",sans-serif;font-size:12px;color:#fff;line-height:20.6px}
.footer-rule{width:1px;height:115px;background:#55607a}
.contact-line{display:flex;align-items:center;gap:6px;font-family:"Roboto Condensed",sans-serif;font-size:10px;color:#fff;line-height:12px}
.social{width:26px;height:26px;border-radius:50%;border:1.5px solid #8c95a6;background:#4a5569}
</style>
</head>
<body>

<footer class="site-footer abs"></footer>

<header class="site-header abs">
  <div class="brand abs">
    <span class="brand-square"></span>
    <span class="brand-name">Tallow Creek Rails</span>
  </div>
  <div class="call-now abs">
    <svg class="abs" style="left:0;top:0" width="230" height="75" viewBox="0 0 230 75">
      <path d="M14 14 C2 30 4 52 20 62" fill="none" stroke="#b80c0c" stroke-width="3"/>
      <path d="M14 58 L22 65 L12 66 Z" fill="#b80c0c"/>
      <path d="M226 14 C238 30 236 52 220 62" fill="none" stroke="#b80c0c" stroke-width="3"/>
      <path d="M226 58 L218 65 L228 66 Z" fill="#b80c0c"/>
      <rect x="38" y="4" width="185" height="32" rx="16" fill="#f7f4ef" stroke="#d8d2c8"/>
      <circle cx="46" cy="20" r="18" fill="#b80c0c"/>
      <circle cx="46" cy="20" r="13" fill="#fff"/>
      <path d="M38 16 q8-6 16 0 l-2 4 h-3 l-1-2 h-4 l-1 2 h-3 Z M40 22 h12 l2 6 h-16 Z" fill="#333"/>
    </svg>
    <span class="call-label abs">CALL NOW</span>
    <span class="call-number abs">03 7420 6618</span>
  </div>
</header>

<nav class="main-nav abs">
  <ul>
    <li>HOME</li><li>PANELSTEEL</li><li>INSTANT QUOTE</li><li>OUR STAFF</li><li>PRODUCTS &amp; SERVICES</li><li>CONTACT US</li>
  </ul>
</nav>

<div class="hero abs" role="img" aria-label="Backyard swimming pool surrounded by a tubular steel pool fence, hedges and lawn"></div>
<h1 class="hero-title abs">Lorem ipsum. Proin gravida nibh vel velit auctor aliquet. Aenean sollicitudin, lorem quis bibendum auctor, nisi elit consequat ipsum, nec sagittis sem nibh id elit.</h1>
<div class="hero-arrow abs" style="left:129px;top:275px"></div>
<div class="hero-arrow abs" style="left:786px;top:275px"></div>
<div class="hero-dots abs"><span></span><span></span><span></span><span></span></div>

<main class="content abs"></main>
<h2 class="h-welcome abs">WELCOME TO TALLOW CREEK RAILS</h2>
<div class="body-copy abs" style="left:140px;top:476px;width:444px">
  <p>Thank you for visiting us at Tallow Creek Rails, my name is Doug and I am the Manager.<br>I built my first fence when I was in my early twenties and have been building fences ever since. Over the last few years we have spent the time looking for fantastic fencing contractors to join our team. Because we only accept the best we have built our business to be one of Victoria's largest fencing contractors.</p>
  <p style="margin-top:12px">At Tallow Creek Rails, we believe in quality above all. The first fence we constructed was over 25 years ago and the number one thing we have learnt is that to do the job right the first time is the best insurance against costly rework.</p>
</div>

<h2 class="h-section abs" style="left:138px;top:589px">OUR SERVICES</h2>
<section class="services abs">
  <ul class="service-list" style="left:13px;top:17px">
    <li><svg width="14" height="13" viewBox="0 0 14 13"><circle cx="6" cy="7" r="5.5" fill="#f0a21c"/><path d="M3 7 l3 3 l7-9" fill="none" stroke="#2f3d52" stroke-width="2"/></svg>Bathroom Remodeling</li>
    <li><svg width="14" height="13" viewBox="0 0 14 13"><circle cx="6" cy="7" r="5.5" fill="#f0a21c"/><path d="M3 7 l3 3 l7-9" fill="none" stroke="#2f3d52" stroke-width="2"/></svg>Attic &amp; Garage Finishing</li>
    <li><svg width="14" height="13" viewBox="0 0 14 13"><circle cx="6" cy="7" r="5.5" fill="#f0a21c"/><path d="M3 7 l3 3 l7-9" fill="none" stroke="#2f3d52" stroke-width="2"/></svg>Carpentry</li>
    <li><svg width="14" height="13" viewBox="0 0 14 13"><circle cx="6" cy="7" r="5.5" fill="#f0a21c"/><path d="M3 7 l3 3 l7-9" fill="none" stroke="#2f3d52" stroke-width="2"/></svg>Tille &amp; Flooring</li>
    <li><svg width="14" height="13" viewBox="0 0 14 13"><circle cx="6" cy="7" r="5.5" fill="#f0a21c"/><path d="M3 7 l3 3 l7-9" fill="none" stroke="#2f3d52" stroke-width="2"/></svg>Decks</li>
  </ul>
  <ul class="service-list" style="left:237px;top:17px">
    <li><svg width="14" height="13" viewBox="0 0 14 13"><circle cx="6" cy="7" r="5.5" fill="#f0a21c"/><path d="M3 7 l3 3 l7-9" fill="none" stroke="#2f3d52" stroke-width="2"/></svg>General Home Maintenance</li>
    <li><svg width="14" height="13" viewBox="0 0 14 13"><circle cx="6" cy="7" r="5.5" fill="#f0a21c"/><path d="M3 7 l3 3 l7-9" fill="none" stroke="#2f3d52" stroke-width="2"/></svg>Painting &amp; Wall Treatments</li>
    <li><svg width="14" height="13" viewBox="0 0 14 13"><circle cx="6" cy="7" r="5.5" fill="#f0a21c"/><path d="M3 7 l3 3 l7-9" fill="none" stroke="#2f3d52" stroke-width="2"/></svg>Drywall Install</li>
    <li><svg width="14" height="13" viewBox="0 0 14 13"><circle cx="6" cy="7" r="5.5" fill="#f0a21c"/><path d="M3 7 l3 3 l7-9" fill="none" stroke="#2f3d52" stroke-width="2"/></svg>Electrical</li>
    <li><svg width="14" height="13" viewBox="0 0 14 13"><circle cx="6" cy="7" r="5.5" fill="#f0a21c"/><path d="M3 7 l3 3 l7-9" fill="none" stroke="#2f3d52" stroke-width="2"/></svg>Fences</li>
  </ul>
</section>

<h2 class="h-section abs" style="left:138px;top:771px">WHEN QUALITY COUNTS, COUNT ON US</h2>
<div class="body-copy abs" style="left:140px;top:793px;width:444px">
  <p>We offer a 12 month workmansh http://tallowcreekrails.com.au/images/bt-arise/aboutus.jpg ip warranty on our fences and will clean the site for free of any debris from the fence construction upon completion of the job. We can offer this workmanship warranty because of our work practices, these include</p>
  <p style="margin-top:12px">6KG of cement in each wooden fence post and 15 – 20KG of concrete for all Steel posts<br>90mm galvanised nails in all rail's rather than industry standard of 75mm<br>75mm galvanised nails in all plinth boards, rather than the industry standard 57mm<br>Timber and Steel all sourced from Industry leaders, rather than the cheapest we can get<br>Gates are all made to order, rather than off the rack. (this means it's always going to be a better fit)</p>
</div>

<div class="quote-banner abs">CLICK FOR INSTANT ONLINE QUOTE</div>
<div class="quote-card abs" role="img" aria-label="Hanging instant quote sign with a small form card"></div>

<aside>
  <section class="widget abs" style="top:447px">
    <div class="widget-head">WHY CHOOSE US</div>
    <div class="widget-photo" role="img" aria-label="Family relaxing together at an outdoor table" style="background:linear-gradient(135deg,#7a9a5a,#d9c6a8 55%,#3b6fa8)"></div>
    <div class="widget-body">We offer a 12 month workmanship warranty on our fences and will clean the site for free of any fencing debris from the fence construction upon completion of the job. We can offer this workmanship warranty</div>
    <div class="widget-btn">FIND OUT MORE ABOUT US<span class="go"><svg width="34" height="24" viewBox="0 0 34 24"><circle cx="17" cy="12" r="7" fill="none" stroke="#fff" stroke-width="1.5"/><path d="M13 12h7M17 9l3 3-3 3" fill="none" stroke="#fff" stroke-width="1.5"/></svg></span></div>
  </section>

  <section class="widget abs" style="top:636px">
    <div class="widget-head">BROCHURES</div>
    <div class="widget-photo" role="img" aria-label="Poolside lounge chair with red cushions in a garden" style="background:linear-gradient(135deg,#3f6b34,#b9b3a4 55%,#c8324a)"></div>
    <div class="widget-body">No pool is complete without a beautiful Pool fence. See our range of Tubular Fencing designs Download our Panelsteel Fencing Brochure and see what a fantastic addition to your home see what a fantastic addition</div>
    <div class="widget-btn">CLICK TO DOWNLOAD NOW<span class="go"><svg width="34" height="24" viewBox="0 0 34 24"><circle cx="17" cy="12" r="7" fill="none" stroke="#fff" stroke-width="1.5"/><path d="M13 12h7M17 9l3 3-3 3" fill="none" stroke="#fff" stroke-width="1.5"/></svg></span></div>
  </section>

  <section class="widget abs" style="top:825px">
    <div class="widget-head">OUR STAFF</div>
    <div class="widget-photo" role="img" aria-label="Glass pool fence beside a blue swimming pool" style="background:linear-gradient(180deg,#2c3a44,#5f8fa6 50%,#2a8fbf)"></div>
    <div class="widget-body">Please feel free to look through our gallery, these are jobs that we have personally done! Please feel free to look through our gallery, these are jobs that we have personally done!</div>
    <div class="widget-btn">SEE SOME OF OUR WORK<span class="go"><svg width="34" height="24" viewBox="0 0 34 24"><circle cx="17" cy="12" r="7" fill="none" stroke="#fff" stroke-width="1.5"/><path d="M13 12h7M17 9l3 3-3 3" fill="none" stroke="#fff" stroke-width="1.5"/></svg></span></div>
  </section>
</aside>

<h3 class="footer-title abs" style="left:138px;top:1035px">BROWSE SITE</h3>
<ul class="footer-menu abs">
  <li>Home</li><li>Panelsteel</li><li>Instant Quote</li><li>Our Staff</li><li>Products &amp; Services</li><li>Contact Us</li>
</ul>
<div class="footer-rule abs" style="left:317px;top:1058px"></div>
<h3 class="footer-title abs" style="left:433px;top:1035px">CONTACT INFO</h3>
<div class="abs" style="left:411px;top:1057px;display:flex;flex-direction:column;gap:8px">
  <div class="contact-line"><svg width="10" height="14" viewBox="0 0 10 14"><path d="M5 0a5 5 0 0 1 5 5c0 4-5 9-5 9S0 9 0 5a5 5 0 0 1 5-5z" fill="#aab2c0"/><circle cx="5" cy="5" r="2" fill="#3b4658"/></svg><span>412 Wattle Bend Road<br>Kyneton, VIC 3444.</span></div>
  <div class="contact-line"><svg width="11" height="9" viewBox="0 0 11 9"><path d="M0 3q5.5-5 11 0l-1 2h-2l-1-1.5h-3L3 5H1z M1 6h9v3H1z" fill="#aab2c0"/></svg><span>+ 61 3 7420 6619</span></div>
  <div class="contact-line"><svg width="11" height="10" viewBox="0 0 11 10"><rect x="2" y="0" width="7" height="3" fill="#aab2c0"/><rect x="0" y="3" width="11" height="5" fill="#aab2c0"/><rect x="2" y="7" width="7" height="3" fill="#dfe3ea"/></svg><span>+ 61 3 7420 6620</span></div>
</div>
<div class="footer-rule abs" style="left:606px;top:1058px"></div>
<h3 class="footer-title abs" style="left:709px;top:1035px">LETS GET SOCIAL</h3>
<div class="social abs" style="left:698px;top:1059px"></div>
<div class="social abs" style="left:733px;top:1059px"></div>
<div class="social abs" style="left:770px;top:1059px"></div>
<div class="social abs" style="left:734px;top:1095px"></div>
<div class="social abs" style="left:770px;top:1095px"></div>
<div class="footer-base abs">Copyright © 2013 TALLOW CREEK RAILS. All rights reserved.</div>

</body>
</html>
```